Pilates 1 on 1 Session

A double sided DL size flyer.

Features

- Harbour Physio Logo (see EPS)
- Pictures only from our photo stock (no random downloaded images).
- Text relevant to the offer we are making (see DL Text file)
- Phone Number and Email Address
- Include photos see URL www.harbourphysio.com.au and those already attached.
- Please incorporate the pilates_studio image file attached as well.

This flyer is designed to bring people in for a 1v1 pilates session with our senior physio. Those who have health insurance will not need to pay anything out of pocket as it is completely covered. After the this session they will then be able to join any one of the other 17 Small pilates groups that we run (by small we mean max of 5 people).

Prefer cool colours like the greens from our logo and perhaps some blue as well.

Cheers

Target Market(s)

Females 20 through to 60 who are interested in fitness and personal health.

Industry/Entity Type

Health

Font styles to use
Sans Serif

Colors
acd036
9bcb3c
0255a3

Requirements
Must have
• Images of pilates equipment that were provided.
Should not have
• Any pictures that have not been supplied either as part of this job or on the website.

```html
<!DOCTYPE html>
<html lang="en">
<head>
<meta charset="utf-8">
<title>Harbour Physio – One Hour Private Pilates Session</title>
<link href="https://fonts.googleapis.com/css2?family=Archivo+Black&family=Lato:wght@700;900&display=swap" rel="stylesheet">
<style>
  :root {
    --green: #9bcb3c;
    --green-light: #acd036;
    --blue: #0255a3;
    --white: #ffffff;
    --photo-top: #d9dcde;
    --photo-bottom: #4a4d52;
  }
  * { margin: 0; padding: 0; box-sizing: border-box; }
  html, body { width: 1200px; height: 2526px; overflow: hidden; background: var(--white); }
  .flyer {
    position: relative;
    width: 1200px;
    height: 2526px;
    overflow: hidden;
    font-family: "Lato", Arial, sans-serif;
    background: var(--white);
  }
  .top-strip {
    position: absolute; left: 0; top: 0;
    width: 758px; height: 44px;
    background: var(--green);
  }
  .side-column {
    position: absolute; left: 758px; top: 0;
    width: 442px; height: 1784px;
    background: var(--blue);
  }
  .brand {
    position: absolute; left: 64px; top: 180px;
    display: flex; align-items: center; gap: 22px;
  }
  .brand-dot {
    width: 70px; height: 70px; border-radius: 50%;
    background: var(--green);
  }
  .brand-name {
    font-family: "Lato", Arial, sans-serif;
    font-weight: 700;
    font-size: 72px;
    line-height: 0.95;
    color: var(--green);
  }
  .headline {
    position: absolute; left: 64px; top: 418px; width: 680px;
    font-family: "Archivo Black", "Arial Black", sans-serif;
    font-size: 68px; line-height: 1.0;
    color: var(--blue);
  }
  .offer-text {
    position: absolute; left: 64px; top: 770px; width: 560px;
    font-weight: 900;
    font-size: 44px; line-height: 1.36;
    color: var(--green);
  }
  .session-note {
    position: absolute; left: 64px; top: 1565px; width: 640px;
    font-weight: 900;
    font-size: 32px; line-height: 1.25;
    color: var(--blue);
    text-transform: uppercase;
  }
  .side-text {
    position: absolute; right: 38px;
    text-align: right;
    color: var(--white);
    font-weight: 900;
  }
  .promise { top: 248px; width: 380px; font-size: 31px; line-height: 1.3; }
  .session-title { top: 440px; width: 340px; font-size: 37px; line-height: 1.3; }
  .cover-band {
    position: absolute; left: 728px; top: 636px;
    width: 472px; height: 84px;
    background: var(--green);
    display: flex; align-items: center; justify-content: center;
    text-align: center;
    color: var(--white);
    font-weight: 900; font-size: 28px; line-height: 1.2;
    text-transform: uppercase;
  }
  .contact { top: 1640px; font-size: 33px; line-height: 1.45; }
  .bottom-band {
    position: absolute; left: 0; top: 1784px;
    width: 1200px; height: 32px;
    background: var(--green);
  }
  .studio-photo {
    position: absolute; left: 0; top: 1816px;
    width: 1200px; height: 710px;
    background: linear-gradient(180deg, var(--photo-top) 0%, #a7abae 45%, var(--photo-bottom) 100%);
  }
</style>
</head>
<body>
<main class="flyer">
  <div class="top-strip"></div>
  <div class="side-column"></div>

  <div class="brand">
    <span class="brand-dot"></span>
    <span class="brand-name">harbour<br>physio</span>
  </div>

  <h1 class="headline">Have you ever wondered about trying Pilates?</h1>

  <p class="offer-text">Experience a one hour session with a principle physio who has 25 years of experience and it will be recovered 100% by your health insurance.</p>

  <p class="session-note">Session lasts an hour and includes a complete physiotherapy assessment.</p>

  <p class="side-text promise">Professional therapists that work with you and your doctor to achieve real results.</p>
  <p class="side-text session-title">One Hour private one-on-one Pilates session</p>

  <div class="cover-band">Covered 100% by your<br>private health insurance</div>

  <p class="side-text contact">Phone: (08) 7100 4821<br>harbourphysio.com.au</p>

  <div class="bottom-band"></div>
  <div class="studio-photo" role="img" aria-label="Photo of the pilates studio with reformer and trapeze equipment, clients exercising on mats and an exercise ball"></div>
</main>
</body>
</html>
```